Zanquorra Business Card Design

Zanquorra is a small and new restaurant/ bar location in Hong Kong. The name "Djibouti" derives from an African country. There is no specific reason behind other than the fact, that the bar is somewhat inspired by African elements (only inspired but not purely based on African cuisine etc.).

The bar is somewhat a fusion of African, Mediterranean and Oriental (Old French Vietnam) elements.

However, it is very imperative to stress, that the overall look and feel of Zanquorra is a very high end cocktail lounge/ bar location. The bar is tucked away in a hidden alley, so people will have to know about it. The idea is to send the consumer off in an Escape or hidden remote location where they are at ease in a hip, stylish and trendy environment.

The card needs to feel high-end.

Final logo artwork has been attached and also pictures of the bar/ restaurant itself. The logo ie monkey head cannot be modified. However, the background color and the color of the type "ZANQUORRA" can be changed.

The following details need to fit onto the business card. Of course they can be arranged to your liking:

LOGO

Colin Vey
Partner

+852 97035164
xxx@zanquorra.com
www.zanquorra.com
7C, Brennick Road, Wan Chai, Hong Kong

```html
<!DOCTYPE html>
<html lang="en">
<head>
<meta charset="utf-8">
<title>Zanquorra Business Card</title>
<link rel="stylesheet" href="https://fonts.googleapis.com/css2?family=Caesar+Dressing&display=swap">
<style>
  :root {
    --backdrop: #4a4a4a;
    --signal-red: #ed1c24;
    --espresso: #241510;
    --espresso-light: #3b2419;
    --cream: #f4efe6;
    --lagoon-blue: #1d6fb8;
    --white: #ffffff;
    --type: "Caesar Dressing", fantasy;
  }
  * { box-sizing: border-box; margin: 0; padding: 0; }
  html, body {
    width: 1200px; height: 1000px; overflow: hidden;
    background: var(--backdrop);
    font-family: var(--type);
  }
  .canvas { position: relative; width: 1200px; height: 1000px; }

  .card {
    position: absolute;
    width: 600px; height: 355px;
    overflow: hidden;
    box-shadow: 0 6px 18px rgba(0,0,0,.35);
  }

  /* Front */
  .card--front { left: 150px; top: 160px; background: var(--espresso); }
  .front__band {
    position: absolute; left: 0; top: 0; width: 100%; height: 185px;
    background: var(--signal-red);
  }
  .front__pattern {
    position: absolute; left: 0; top: 185px; width: 100%; height: 170px;
    background: linear-gradient(135deg, var(--espresso) 0%, var(--espresso-light) 50%, var(--espresso) 100%);
  }
  .front__emblem {
    position: absolute; left: 50%; top: 28px; transform: translateX(-50%);
    width: 150px; height: 150px; border-radius: 50%;
    background: var(--cream); border: 3px solid var(--espresso);
  }
  .front__name {
    position: absolute; left: 0; right: 0; top: 205px;
    text-align: center; color: var(--white);
    font-size: 74px; letter-spacing: 2px; line-height: 1;
  }

  /* Back */
  .card--back { left: 430px; top: 580px; background: var(--espresso); }
  .back__pattern {
    position: absolute; left: 0; top: 0; width: 100%; height: 170px;
    background: linear-gradient(135deg, var(--espresso) 0%, var(--espresso-light) 50%, var(--espresso) 100%);
  }
  .back__emblem {
    position: absolute; left: 100px; top: 28px;
    width: 72px; height: 72px; border-radius: 50%;
    background: var(--cream); border: 2px solid var(--espresso);
  }
  .back__name {
    position: absolute; left: 36px; top: 108px;
    color: var(--lagoon-blue); font-size: 34px; line-height: 1;
  }
  .person {
    position: absolute; right: 30px; top: 32px; text-align: center;
  }
  .person__name { color: var(--white); font-size: 20px; letter-spacing: 1px; line-height: 1.1; }
  .person__role { color: var(--signal-red); font-size: 16px; letter-spacing: 1px; line-height: 1.1; }

  .contacts {
    position: absolute; left: 0; right: 0; top: 190px;
    list-style: none; text-align: center;
  }
  .contacts li {
    color: var(--white); font-size: 15px; letter-spacing: .5px;
    height: 39px; line-height: 39px;
  }
  .contacts svg { width: 12px; height: 12px; vertical-align: -1px; margin-right: 8px; fill: var(--signal-red); }
</style>
</head>
<body>
<main class="canvas">

  <section class="card card--front" aria-label="Business card front">
    <div class="front__band"></div>
    <div class="front__pattern" role="img" aria-label="Dark brown interlocking geometric pattern"></div>
    <div class="front__emblem"></div>
    <h1 class="front__name">ZANQUORRA</h1>
  </section>

  <section class="card card--back" aria-label="Business card back">
    <div class="back__pattern" role="img" aria-label="Dark brown interlocking geometric pattern"></div>
    <div class="back__emblem"></div>
    <p class="back__name">ZANQUORRA</p>

    <div class="person">
      <p class="person__name">COLIN VEY</p>
      <p class="person__role">PARTNER</p>
    </div>

    <ul class="contacts">
      <li><svg viewBox="0 0 12 12"><path d="M2.5 0.5l2 2.5-1.2 1.4c.7 1.6 2 2.9 3.6 3.6l1.4-1.2 2.5 2-1.3 2.2C5 10.5 1.5 7 .3 1.8z"/></svg>+852 97035164</li>
      <li><svg viewBox="0 0 12 12"><path d="M0 2h12v8H0zM1 3v.4l5 3.3 5-3.3V3zm0 1.6V9h10V4.6L6 8z"/></svg>xxx@zanquorra.com</li>
      <li><svg viewBox="0 0 12 12"><circle cx="6" cy="6" r="5.5"/></svg>www.zanquorra.com</li>
      <li><svg viewBox="0 0 12 12"><path d="M6 0a4 4 0 0 1 4 4c0 3-4 8-4 8S2 7 2 4a4 4 0 0 1 4-4zm0 2.4A1.6 1.6 0 1 0 6 5.6 1.6 1.6 0 0 0 6 2.4z"/></svg>7C, Brennick Road, Wan Chai, Hong Kong</li>
    </ul>
  </section>

</main>
</body>
</html>
```